Brindle Office - One sheet needed for Sales Team

We need a One Sheet that introduces our business and what we do to prospective customers. This will be used both digitally and print for sales calls, both virtually and in person. Ideally we'd like this to match our branding and messaging from our website brindleofficeco.com so there is consistency with our messaging. Also, we have a desire for this to have a call to action that directs to our website and main phone where we have lead capture ability.
It should be clean and consistent with current marketing trends. We would like to include information about the business, our value proposition of being able to save customers up to 60% off their copy and printing costs, and some differentiators (i.e. 80+ point inspection of equipment, full teardown and rebuild of like new units, transparent pricing and lease options, 6 month warranty, comprehensive maintenance programs).

```html
<!DOCTYPE html>
<html lang="en">
<head>
<meta charset="utf-8">
<title>Brindle Office – One Sheet</title>
<link href="https://fonts.googleapis.com/css2?family=Montserrat:wght@500;700;800;900&display=swap" rel="stylesheet">
<style>
  :root{
    --stage:#222222;
    --ink:#161616;
    --white:#ffffff;
    --blue:#0a9ee0;
    --magenta:#cc2862;
    --yellow:#fff000;
    --paper:#f3f3f3;
    --rule:rgba(255,255,255,.35);
  }
  *{margin:0;padding:0;box-sizing:border-box}
  html,body{width:1105px;height:1200px;overflow:hidden;background:var(--stage);font-family:"Montserrat",Arial,sans-serif}
  .sheet{position:absolute;left:160px;top:79px;width:785px;height:1016px;background:var(--white);overflow:hidden}
  .sheet-shapes{position:absolute;inset:0;width:785px;height:1016px}
  .brand{position:absolute;left:48px;top:48px;display:flex;align-items:center;gap:10px}
  .brand-dot{width:18px;height:18px;border-radius:50%;background:var(--magenta)}
  .brand-name{font-weight:900;font-size:31px;color:var(--ink);letter-spacing:-.5px;line-height:1}
  .headline{position:absolute;left:36px;top:176px;font-weight:900;line-height:1;color:var(--white)}
  .headline span{display:block}
  .headline .small{font-size:35px;letter-spacing:-.5px}
  .headline .big{font-size:55px;color:var(--yellow);letter-spacing:-1.5px;margin-top:6px}
  .headline .big + .big{margin-top:4px}
  .headline .small.last{margin-top:10px}
  .about{position:absolute;left:36px;top:458px;width:306px;color:var(--ink)}
  .about h2{font-weight:900;font-size:24.5px;letter-spacing:-.5px;line-height:1;margin-bottom:16px;white-space:nowrap}
  .about p{font-size:13.2px;font-weight:500;line-height:15px;text-align:justify;color:#222}
  .about p + p{margin-top:20px}
  .about p.cont{margin-top:0}
  .benefits{position:absolute;left:405px;top:432px;width:353px;list-style:none}
  .benefits li{display:flex;align-items:center;gap:12px;color:var(--white);font-weight:800;font-size:14px;letter-spacing:0;white-space:nowrap;height:48px;border-bottom:1px solid var(--rule)}
  .benefits li:last-child{border-bottom:none;height:58px}
  .benefits svg{flex:none}
  .offer{position:absolute;left:359px;top:704px;width:426px;height:189px;text-align:center;font-weight:900;line-height:1}
  .offer .pct{display:block;font-size:71px;color:var(--ink);letter-spacing:-1px;margin-top:16px}
  .offer .line{display:block;font-size:42px;color:var(--magenta);letter-spacing:-.5px;margin-top:6px}
  .offer .line b{color:var(--ink);font-weight:900}
  .cta{position:absolute;left:46px;top:928px}
  .cta .lead{display:block;font-weight:800;font-size:20px;color:var(--ink);line-height:1}
  .cta .action{display:block;font-weight:900;font-size:38px;color:var(--magenta);line-height:1;margin-top:2px}
  .contact{position:absolute;left:354px;top:904px;color:var(--white);font-weight:900;line-height:1}
  .contact div{display:flex;align-items:center;gap:14px}
  .contact .web{font-size:27px}
  .contact .phone{font-size:36px;margin-top:14px}
</style>
</head>
<body>
<main class="sheet">
  <svg class="sheet-shapes" viewBox="0 0 785 1016">
    <defs>
      <linearGradient id="paperFade" x1="0" y1="0" x2="1" y2="1">
        <stop offset="0" stop-color="#ececec"/><stop offset=".6" stop-color="#fafafa"/><stop offset="1" stop-color="#f1f1f1"/>
      </linearGradient>
      <linearGradient id="showroom" x1="0" y1="0" x2="0" y2="1">
        <stop offset="0" stop-color="#5b6066"/><stop offset=".55" stop-color="#8b9095"/><stop offset="1" stop-color="#6d7176"/>
      </linearGradient>
      <linearGradient id="officeTint" x1="0" y1="0" x2="1" y2="1">
        <stop offset="0" stop-color="#0a9ee0"/><stop offset=".7" stop-color="#1aa3dc"/><stop offset="1" stop-color="#3a9cc4"/>
      </linearGradient>
      <linearGradient id="topFade" x1="0" y1="0" x2="1" y2="0">
        <stop offset="0" stop-color="#ffffff"/><stop offset="1" stop-color="#e9e9e9"/>
      </linearGradient>
    </defs>
    <rect x="0" y="0" width="785" height="127" fill="url(#topFade)"/>
    <rect x="0" y="422" width="785" height="594" fill="url(#paperFade)"/>
    <polygon points="263,127 472,127 559,33 785,33 785,422 263,422" fill="url(#showroom)" role="img" aria-label="Photo of a large office multifunction copier in a grey showroom"/>
    <polyline points="263,123 474,123 561,29 785,29" fill="none" stroke="var(--magenta)" stroke-width="9"/>
    <rect x="0" y="118" width="263" height="10" rx="5" fill="var(--ink)"/>
    <circle cx="263" cy="123" r="5" fill="var(--white)"/>
    <rect x="0" y="128" width="371" height="294" fill="url(#officeTint)" role="img" aria-label="Blue-tinted photo of an office reception desk"/>
    <polygon points="371,388 785,422 785,704 371,704" fill="var(--magenta)"/>
    <polygon points="359,704 371,694 371,704" fill="var(--ink)"/>
    <rect x="359" y="704" width="426" height="189" fill="var(--yellow)"/>
    <polygon points="354,893 785,893 785,1016 0,1016 0,995 303,995" fill="var(--blue)"/>
    <polygon points="341,893 354,893 303,995 288,995" fill="var(--ink)"/>
  </svg>

  <div class="brand">
    <span class="brand-dot"></span>
    <span class="brand-name">BRINDLE OFFICE</span>
  </div>

  <h1 class="headline">
    <span class="small">HELPING</span>
    <span class="big">BUSINESS</span>
    <span class="big">OWNERS</span>
    <span class="small last">SAVE MONEY</span>
  </h1>

  <section class="about">
    <h2>About Brindle Office</h2>
    <p>Brindle Office was formed in 1986, and has been serving the DFW community for over three decades as a premier copier sales, service, and rental co. We offer the finest in state of the art equipment from manufacturers such as Norvale, Kestra, and Halden Vista.</p>
    <p>Brindle Office offers the finest in state of the art equipment from manufacturers such as Norvale, Kestra, and Halden Vista. In addition to new equipment, we also rent, lease, and sell refurbished copiers. These copiers are fully reconditioned and warranted to give many years of high quality performance to the cost conscious business.</p>
    <p class="cont">Since we carry over a million dollars in supplies and parts, Brindle Office is able to provide maintenance agreements on most copiers. We offer a two hour response time on all repairs within the DFW Metroplex. Our technicians have a minimum of 10 years repair experience and a combined total of 79 years!</p>
  </section>

  <ul class="benefits">
    <li><svg width="18" height="16" viewBox="0 0 18 16"><rect x="1" y="3" width="12" height="12" rx="2" fill="none" stroke="#fff" stroke-width="2"/><path d="M4 9l3 3 9-10" fill="none" stroke="#fff" stroke-width="2.4"/></svg>80+ point inspection of equipment</li>
    <li><svg width="18" height="16" viewBox="0 0 18 16"><rect x="1" y="3" width="12" height="12" rx="2" fill="none" stroke="#fff" stroke-width="2"/><path d="M4 9l3 3 9-10" fill="none" stroke="#fff" stroke-width="2.4"/></svg>Transparent pricing and lease options</li>
    <li><svg width="18" height="16" viewBox="0 0 18 16"><rect x="1" y="3" width="12" height="12" rx="2" fill="none" stroke="#fff" stroke-width="2"/><path d="M4 9l3 3 9-10" fill="none" stroke="#fff" stroke-width="2.4"/></svg>6 month warranty</li>
    <li><svg width="18" height="16" viewBox="0 0 18 16"><rect x="1" y="3" width="12" height="12" rx="2" fill="none" stroke="#fff" stroke-width="2"/><path d="M4 9l3 3 9-10" fill="none" stroke="#fff" stroke-width="2.4"/></svg>Full teardown and rebuild&nbsp; new units</li>
    <li><svg width="18" height="16" viewBox="0 0 18 16"><rect x="1" y="3" width="12" height="12" rx="2" fill="none" stroke="#fff" stroke-width="2"/><path d="M4 9l3 3 9-10" fill="none" stroke="#fff" stroke-width="2.4"/></svg>Comprehensive maintenance programs</li>
  </ul>

  <div class="offer">
    <span class="pct">60% OFF</span>
    <span class="line">ON COPY <b>AND</b></span>
    <span class="line">PRINTING COST</span>
  </div>

  <div class="cta">
    <span class="lead">For more information</span>
    <span class="action">Contact us</span>
  </div>

  <div class="contact">
    <div class="web">
      <svg width="24" height="24" viewBox="0 0 24 24"><circle cx="12" cy="12" r="10" fill="none" stroke="var(--yellow)" stroke-width="2"/><ellipse cx="12" cy="12" rx="4.5" ry="10" fill="none" stroke="var(--yellow)" stroke-width="1.8"/><path d="M2 12h20M4 7h16M4 17h16" stroke="var(--yellow)" stroke-width="1.6"/></svg>
      brindleofficeco.com
    </div>
    <div class="phone">
      <svg width="24" height="24" viewBox="0 0 24 24"><path d="M6 2l4 5-2 3c1.5 3 3.5 5 6 6l3-2 5 4-3 4C10 21 3 14 2 5z" fill="var(--yellow)"/></svg>
      +1 972-555-0148
    </div>
  </div>
</main>
</body>
</html>
```